Menu Design Project

This is a sushi menu. We need to polish the menu. You can re-size logo and add color and graphic to make inviting. Please feel free to make any recommendations.

Upscale crowd

```html
<!DOCTYPE html>
<html lang="en">
<head>
<meta charset="utf-8">
<title>Kaido Sushi Bar — Menu</title>
<link href="https://fonts.googleapis.com/css2?family=Oswald:wght@400;700&family=Archivo+Narrow:wght@400;700&display=swap" rel="stylesheet">
<style>
:root{
  --red:#c8161d;
  --red-dark:#8e0e12;
  --ink:#1b1b1b;
  --paper:#ffffff;
  --panel:#ececec;
  --stage:#e4e1dc;
  --photo-a:#e9b59a;
  --photo-b:#d8573a;
  --photo-c:#f3efe8;
}
*{box-sizing:border-box;margin:0;padding:0}
html,body{width:1200px;height:1000px;overflow:hidden}
body{background:var(--stage);font-family:"Archivo Narrow",Arial,sans-serif;color:var(--ink);position:relative}
.spread{position:absolute;top:60px;left:20px;width:1160px;height:880px;display:flex;gap:20px}
.page{position:relative;width:570px;height:880px;background:var(--paper);overflow:hidden;box-shadow:0 4px 14px rgba(0,0,0,.25)}
.page__band{position:absolute;top:0;bottom:0;width:22px;background:var(--red)}
.page__band--left{left:0}
.page__band--right{right:0}
.page__body{position:absolute;top:16px;left:32px;right:32px;bottom:112px;display:grid;gap:12px;overflow:hidden}
.page--left .page__body{grid-template-columns:1fr 1.05fr 0.95fr}
.page--right .page__body{grid-template-columns:1fr 1fr 1fr}
.col{overflow:hidden}
.brand{text-align:center;padding:6px 0 10px}
.brand__mark{width:70px;height:70px;border-radius:50%;background:var(--red);margin:0 auto 12px}
.brand__name{font-family:"Oswald",Arial,sans-serif;font-weight:700;font-size:38px;line-height:1;letter-spacing:1px;color:var(--ink)}
.brand__sub{font-family:"Oswald",Arial,sans-serif;font-weight:400;font-size:17px;letter-spacing:4px;color:var(--ink);margin-top:2px}
.heading{display:flex;align-items:center;gap:4px;margin:8px 0 5px}
.heading::before,.heading::after{content:"";flex:1;height:5px;background:linear-gradient(to bottom,var(--ink) 0 2px,transparent 2px 3px,var(--red) 3px 5px)}
.heading span{font-family:"Oswald",Arial,sans-serif;font-weight:700;font-size:9px;letter-spacing:3px;text-transform:uppercase}
.note{font-size:6.5px;font-style:italic;text-align:center;margin:-2px 0 4px}
.item{font-size:7.3px;line-height:1.3;margin-bottom:3.5px}
.item b{font-weight:700}
.price{font-weight:700;margin-left:2px}
.specials{background:var(--panel);padding:2px 6px 6px;margin-bottom:6px}
.pairs{display:grid;grid-template-columns:1fr 20px 1fr 20px;font-size:7.3px;line-height:1.38;column-gap:3px}
.pairs .p{font-weight:700;text-align:right}
.smalllist{display:grid;grid-template-columns:1fr 1fr;gap:2px 8px}
.disclaimer{position:absolute;left:40px;right:40px;bottom:104px;font-size:6px;font-style:italic;text-align:center}
.photo-strip{position:absolute;left:22px;right:22px;bottom:0;height:98px;background:linear-gradient(90deg,var(--photo-c) 0%,var(--photo-a) 22%,var(--photo-b) 45%,var(--photo-c) 62%,var(--photo-b) 80%,var(--photo-c) 100%)}
</style>
</head>
<body>
<main class="spread">

  <section class="page page--left">
    <div class="page__band page__band--left" role="img" aria-label="Red border with gold floral ornament"></div>
    <div class="page__band page__band--right" role="img" aria-label="Red border with gold floral ornament"></div>
    <div class="page__body">
      <div class="col">
        <header class="brand">
          <div class="brand__mark"></div>
          <div class="brand__name">KAIDO</div>
          <div class="brand__sub">SUSHI BAR</div>
        </header>
        <h2 class="heading"><span>Appetizers</span></h2>
        <p class="item"><b>edamame</b> soybeans &amp; sea salt <span class="price">3.5</span></p>
        <p class="item"><b>spicy garlic edamame</b> soybeans, sea salt &amp; spicy garlic <span class="price">4.5</span></p>
        <p class="item"><b>sautéed asparagus</b> asparagus &amp; teriyaki sauce <span class="price">4.5</span></p>
        <p class="item"><b>sautéed shiitake</b> mushrooms, onions &amp; cream sauce <span class="price">5</span></p>
        <p class="item"><b>age dashi tofu</b> tofu, sweet dashi soy sauce &amp; bonito flakes <span class="price">5</span></p>
        <p class="item"><b>yakitori</b> teriyaki chicken &amp; vegetables served on skewers <span class="price">6</span></p>
        <p class="item"><b>gyoza</b> beef &amp; vegetable dumplings <span class="price">5.5</span></p>
        <p class="item"><b>shumai</b> shrimp dumplings &amp; ponzu sauce <span class="price">5.5</span></p>
        <p class="item"><b>soft-shell crab</b> fried soft-shell crab &amp; ponzu sauce <span class="price">9</span></p>
        <p class="item"><b>tatsuta-age</b> panko breaded chicken, garlic &amp; teriyaki sauce <span class="price">6</span></p>
        <p class="item"><b>tako su</b> octopus marinated in citrus sauce <span class="price">7</span></p>
        <p class="item"><b>calamari rings</b> fried calamari &amp; tempura sauce <span class="price">8</span></p>
        <p class="item"><b>grilled calamari</b> grilled calamari marinated in lemon teriyaki sauce, garlic &amp; ginger <span class="price">8</span></p>
        <p class="item"><b>hamachi kama</b> yellowtail collar &amp; ponzu sauce <span class="price">8</span></p>
        <p class="item"><b>mixed tempura</b> tempura shrimp &amp; vegetables <span class="price">7</span></p>
        <p class="item"><b>vegetable tempura</b> tempura vegetables <span class="price">6</span></p>
        <p class="item"><b>chicken katsu</b> breaded chicken skewers &amp; japanese barbecue sauce <span class="price">5.5</span></p>
        <h2 class="heading"><span>Soup</span></h2>
        <p class="item"><b>miso soup</b> tofu, scallions, seaweed &amp; miso broth <span class="price">2</span></p>
        <p class="item"><b>mushroom miso soup</b> tofu, scallions, enoki &amp; shiitake <span class="price">4</span></p>
        <p class="item"><b>suimono</b> japanese clear soup <span class="price">2</span></p>
        <p class="item"><b>ishikari nabe</b> salmon, miso broth &amp; vegetables <span class="price">8</span></p>
        <h2 class="heading"><span>Salads</span></h2>
        <p class="item"><b>house salad</b> mixed greens, vegetables &amp; ginger dressing <span class="price">2.5</span></p>
        <p class="item"><b>tofu salad</b> house salad, tofu, bonito flakes &amp; sesame dressing <span class="price">4</span></p>
        <p class="item"><b>seaweed salad</b> marinated seaweed, sesame seeds &amp; sesame oil <span class="price">4</span></p>
        <p class="item"><b>avocado salad</b> house salad &amp; avocado <span class="price">4</span></p>
      </div>

      <div class="col">
        <p class="item"><b>spicy tuna salad*</b> spicy tuna, cucumber, masago, daikon, spring mix &amp; citrus sauce <span class="price">10</span></p>
        <p class="item"><b>crab salad</b> crab salad, cucumber, daikon, spring mix &amp; sesame dressing <span class="price">8</span></p>
        <p class="item"><b>spicy seafood salad*</b> shrimp, spicy scallop, crabstick, cucumber, daikon, spring mix &amp; sesame dressing <span class="price">10</span></p>
        <p class="item"><b>ika salad</b> squid salad &amp; japanese mountain vegetables <span class="price">6.5</span></p>
        <h2 class="heading"><span>Noodles</span></h2>
        <p class="item"><b>mori soba</b> chilled buckwheat noodles &amp; dipping sauce <span class="price">7</span></p>
        <p class="item"><b>tempura udon</b> japanese udon noodles, shrimp, seafood &amp; vegetable tempura <span class="price">10</span></p>
        <p class="item"><b>kake udon</b> japanese udon noodles, clear broth, scallions, seaweed, fried tofu &amp; fish cake <span class="price">7</span></p>
        <p class="item"><b>yaki udon</b> stir-fried chicken, cabbage, onions, scallions, carrots, bean sprouts &amp; seaweed flakes <span class="price">10</span></p>
        <p class="item"><b>vegetable udon</b> japanese udon noodles, vegetables, tofu &amp; clear broth <span class="price">8</span></p>
        <p class="item"><b>nabeyaki udon</b> japanese udon noodles, egg &amp; shrimp tempura <span class="price">11</span><br><b>add seafood</b> (mussels, shrimp, scallop &amp; calamari) <span class="price">13</span></p>
        <p class="item"><b>spicy seafood udon</b> sautéed shrimp, scallop, calamari, mussels, asparagus, zucchini &amp; carrots <span class="price">15</span></p>
        <p class="item"><b>yakisoba</b> stir-fried soba noodles &amp; vegetables<br><b>beef</b> <span class="price">11</span> <b>seafood</b> (shrimp, scallop &amp; calamari) <span class="price">13</span></p>
        <p class="item"><b>seafood noodle soup</b> noodle soup, vegetables, mussels, shrimp, scallop &amp; calamari <span class="price">13</span></p>
        <h2 class="heading"><span>Entrees</span></h2>
        <p class="item"><b>teriyaki</b> teriyaki sauce, sesame seeds &amp; vegetables served with a side of miso soup, house salad &amp; rice<br><b>salmon</b> <span class="price">15</span> · <b>chicken</b> <span class="price">12</span> · <b>beef</b> <span class="price">15</span><br><b>beef &amp; chicken</b> <span class="price">18</span><br><b>salmon w/ shrimp &amp; vegetable tempura</b> <span class="price">17</span><br><b>chicken w/ shrimp &amp; vegetable tempura</b> <span class="price">16</span><br><b>beef w/ shrimp &amp; vegetable tempura</b> <span class="price">17</span></p>
        <p class="item"><b>katsu</b> breaded cutlet, japanese barbecue sauce &amp; shredded cabbage served with miso soup, house salad &amp; rice<br><b>chicken</b> <span class="price">12</span> · <b>beef</b> <span class="price">15</span> · <b>tonkatsu</b> (pork loin) <span class="price">13</span><br><b>tonkatsu w/ shrimp &amp; vegetable tempura</b> <span class="price">18</span></p>
        <p class="item"><b>tempura</b> lightly battered &amp; fried with a side of sauce served with miso soup, house salad &amp; rice<br><b>vegetable</b> <span class="price">10</span> · <b>shrimp &amp; vegetable</b> <span class="price">17</span></p>
        <p class="item"><b>negimaki</b> sliced meat, scallions &amp; teriyaki sauce served with miso soup, house salad &amp; rice<br><b>chicken</b> <span class="price">12</span> · <b>beef</b> <span class="price">15</span></p>
        <p class="item"><b>asparagus maki</b> sliced beef, asparagus &amp; teriyaki sauce served with a side of miso soup, house salad &amp; rice <span class="price">15</span></p>
        <p class="item"><b>bibimbap</b> rice, carrots, beansprouts, daikon, spinach, zucchini, sesame seeds, seaweed flakes, a fried egg &amp; spicy sauce with miso soup &amp; house salad<br><b>tofu</b> <span class="price">11</span> · <b>chicken</b> <span class="price">12</span> · <b>beef</b> <span class="price">13</span></p>
        <p class="item"><b>bulgogi</b> thinly sliced beef, carrots &amp; onions served with a side of miso soup, house salad &amp; rice <span class="price">14</span></p>
      </div>

      <div class="col">
        <div class="specials">
          <h2 class="heading"><span>Specials</span></h2>
          <p class="note">lunch specials offered 11am–2:30pm, mon–sat</p>
          <p class="item"><b>chicken (9), beef or salmon teriyaki</b> <span class="price">10</span></p>
          <p class="item"><b>tonkatsu</b> (pork loin) <span class="price">10</span></p>
          <p class="item"><b>shrimp &amp; vegetable tempura</b> <span class="price">10</span></p>
          <p class="item"><b>chicken &amp; beef teriyaki</b> <span class="price">11</span></p>
          <p class="item"><b>beef teriyaki w/ shrimp &amp; vegetable tempura</b> <span class="price">11</span></p>
          <p class="item"><b>chicken teriyaki w/ shrimp &amp; vegetable tempura</b> <span class="price">11</span></p>
          <p class="item"><b>salmon teriyaki w/ shrimp &amp; vegetable tempura</b> <span class="price">11</span></p>
          <p class="item"><b>tonkatsu w/ shrimp &amp; vegetable tempura</b> <span class="price">11</span></p>
          <p class="item"><b>bento box</b> fried rice, vegetable tempura, fruit, house special, miso soup &amp; house salad<br><b>beef teriyaki</b> 12 · <b>chicken teriyaki</b> 11<br><b>salmon teriyaki</b> 12 · <b>shrimp tempura</b> 11<br><b>chicken katsu</b> 11 · <b>tonkatsu</b> 11</p>
          <p class="item"><b>nigiri box*</b> sashimi (2 pcs of each) salmon, tuna, red snapper &amp; white tuna, nigiri &amp; rice <span class="price">15</span></p>
          <p class="item"><b>omakase special*</b> nigiri (5 pcs) &amp; california roll <span class="price">12</span></p>
          <p class="item"><b>omakase deluxe*</b> nigiri (6 pcs) &amp; spicy tuna roll <span class="price">13</span></p>
          <p class="item"><b>maki combo*</b> california roll, cucumber roll &amp; tuna roll <span class="price">9</span></p>
          <p class="item"><b>maki combo special*</b> spicy tuna, avocado roll &amp; salmon roll <span class="price">10</span></p>
          <p class="item"><b>chirashi*</b> assorted raw fish &amp; vegetables over rice <span class="price">11</span></p>
        </div>
        <h2 class="heading"><span>Sides</span></h2>
        <p class="item"><b>steamed rice</b> <span class="price">1.5</span></p>
        <p class="item"><b>brown rice</b> <span class="price">1.5</span></p>
        <p class="item"><b>sushi rice</b> <span class="price">2</span></p>
        <p class="item"><b>avocado</b> <span class="price">1.5</span></p>
        <p class="item"><b>tofu</b> <span class="price">1</span></p>
        <p class="item"><b>shrimp tempura</b> (1 pc.) <span class="price">2</span></p>
        <p class="item"><b>teriyaki sauce</b> <span class="price">0.5</span></p>
        <p class="item"><b>ginger dressing</b> <span class="price">0.5</span></p>
        <h2 class="heading"><span>Drinks</span></h2>
        <p class="item"><b>cola</b></p>
        <p class="item"><b>diet cola</b></p>
        <p class="item"><b>lemon-lime soda</b></p>
        <p class="item"><b>orange soda</b></p>
        <p class="item"><b>orange or apple juice</b> (no refills)</p>
        <p class="item"><b>lemonade</b></p>
        <p class="item"><b>iced tea</b></p>
        <p class="item"><b>hot japanese green tea</b></p>
        <h2 class="heading"><span>Dessert</span></h2>
        <p class="item"><b>frushi</b> seasonal fruit wrapped in a maki roll <span class="price">8</span></p>
        <p class="item"><b>mochi ice cream</b> japanese confection with ice cream filling <span class="price">4</span></p>
        <p class="item"><b>tempura ice cream</b> fried vanilla ice cream with caramel <span class="price">3.5</span></p>
      </div>
    </div>
    <p class="disclaimer">*These foods contain raw seafood. Consuming raw or partially cooked seafood may increase your risk of foodborne illness. Prices subject to change.</p>
    <div class="photo-strip" role="img" aria-label="Photographs of sashimi, salmon rolls and shrimp nigiri plated on white dishes"></div>
  </section>

  <section class="page page--right">
    <div class="page__band page__band--left" role="img" aria-label="Red border with gold floral ornament"></div>
    <div class="page__band page__band--right" role="img" aria-label="Red border with gold floral ornament"></div>
    <div class="page__body">
      <div class="col">
        <h2 class="heading"><span>Signature Maki</span></h2>
        <p class="item"><b>rainbow*</b> crab mix topped with assorted fish <span class="price">10</span></p>
        <p class="item"><b>alaska</b> crab mix &amp; avocado topped with baked spicy salmon &amp; unagi sauce <span class="price">10</span></p>
        <p class="item"><b>butterfly*</b> spicy hamachi, cucumber &amp; scallions topped with avocado &amp; unagi sauce <span class="price">10</span></p>
        <p class="item"><b>golden sun</b> tempura crab mix, avocado &amp; unagi sauce <span class="price">7</span></p>
        <p class="item"><b>caterpillar</b> unagi &amp; cucumber topped with avocado <span class="price">9.5</span></p>
        <p class="item"><b>sunkiss*</b> spicy tuna topped with salmon &amp; avocado <span class="price">9.5</span></p>
        <p class="item"><b>white tuna delight*</b> yellowtail, cucumber &amp; kaiware topped with white tuna, scallions &amp; spicy sauce <span class="price">9.5</span></p>
        <p class="item"><b>premium alaska</b> shrimp tempura, unagi, cucumber &amp; cream cheese topped with baked spicy crab salad &amp; special sauce <span class="price">11</span></p>
        <p class="item"><b>orange blossom*</b> crab mix roll topped with salmon, scallions &amp; spicy sauce <span class="price">9.5</span></p>
        <p class="item"><b>tuna fantastic*</b> white tuna, cucumber, scallions &amp; lemon zest topped with tuna &amp; wasabi sauce <span class="price">9.5</span></p>
        <p class="item"><b>yellowtail special*</b> scallions, cucumber &amp; avocado topped with yellowtail, jalapeño &amp; citrus sauce <span class="price">9.5</span></p>
        <p class="item"><b>snow white tuna*</b> shrimp tempura &amp; spicy tuna topped with white tuna, scallions &amp; special sauce <span class="price">10</span></p>
        <p class="item"><b>super titan*</b> deep-fried yellowtail, cream cheese &amp; avocado topped with spicy tuna &amp; scallions <span class="price">10</span></p>
        <p class="item"><b>smoked salmon lover</b> crab, cream cheese, cucumber &amp; smoked salmon topped with avocado <span class="price">9.5</span></p>
        <p class="item"><b>geisha*</b> salmon, tuna, white fish, scallions &amp; kaiware wrapped in soy paper with sesame seeds <span class="price">10</span></p>
        <p class="item"><b>unagi lover</b> deep-fried freshwater eel, crab, cream cheese &amp; scallions rolled in seaweed topped with unagi sauce <span class="price">9.5</span></p>
        <p class="item"><b>garden</b> avocado, asparagus, cucumber, oshinko &amp; kaiware wrapped in rice &amp; seaweed <span class="price">7</span></p>
        <p class="item"><b>fire tuna*</b> cucumber, unagi &amp; shrimp roll topped with spicy tuna, tempura flakes &amp; jalapeño <span class="price">10</span></p>
        <p class="item"><b>spicy crunchy tuna*</b> spicy tuna, cucumber &amp; avocado wrapped in tempura flakes topped with spicy sauce <span class="price">7</span></p>
        <p class="item"><b>hearts on fire*</b> spicy tuna, salmon &amp; avocado topped with red snapper, jalapeño &amp; spicy sauce <span class="price">9.5</span></p>
        <p class="item"><b>philadelphia</b> smoked salmon, cream cheese &amp; cucumber <span class="price">6</span></p>
        <p class="item"><b>fantasy eel*</b> spicy scallops &amp; salmon topped with unagi &amp; avocado <span class="price">10</span></p>
        <p class="item"><b>las vegas</b> deep-fried salmon, avocado &amp; cream cheese topped with jalapeño &amp; spicy sauce <span class="price">8</span></p>
        <p class="item"><b>salmon asparagus*</b> crab mix, cucumber &amp; asparagus topped with salmon <span class="price">9</span></p>
        <p class="item"><b>vegetable tempura</b> battered asparagus &amp; sweet potato topped with crunchy tempura bits <span class="price">7</span></p>
        <p class="item"><b>lollipop*</b> tuna, salmon, spicy white tuna, crab &amp; lettuce wrapped in cucumber with ponzu sauce <span class="price">9</span></p>
        <p class="item"><b>volcano shrimp tempura</b> shrimp tempura &amp; cucumber topped with baked scallops &amp; masago <span class="price">11</span></p>
        <p class="item"><b>dancing shrimp</b> crab mix, avocado &amp; cucumber topped with cooked shrimp &amp; unagi sauce <span class="price">10</span></p>
      </div>

      <div class="col">
        <p class="item"><b>crazy</b> grilled salmon skin, unagi, avocado &amp; kaiware topped with unagi sauce &amp; special sauce <span class="price">9</span></p>
        <p class="item"><b>shrimp tempura</b> shrimp tempura, crab stick, avocado &amp; kaiware topped with sesame seeds <span class="price">8.5</span></p>
        <p class="item"><b>spider</b> soft-shell crab, crab stick, avocado &amp; kaiware topped with sesame seeds <span class="price">9</span></p>
        <p class="item"><b>atlantic</b> deep-fried salmon &amp; cream cheese <span class="price">6</span></p>
        <p class="item"><b>monster shrimp</b> shrimp tempura, avocado &amp; cucumber topped with crab mix &amp; shrimp with special spicy sauce <span class="price">9</span></p>
        <p class="item"><b>big bang*</b> crab stick, cucumber, shrimp &amp; cream cheese topped with spicy tuna, seaweed salad &amp; masago <span class="price">11</span></p>
        <p class="item"><b>dragon</b> shrimp tempura &amp; crab stick topped with unagi, avocado &amp; unagi sauce <span class="price">11</span></p>
        <p class="item"><b>chicken teriyaki</b> grilled chicken breast &amp; cucumber topped with teriyaki sauce <span class="price">7.5</span></p>
        <h2 class="heading"><span>Traditional Maki</span></h2>
        <p class="note">all traditional maki may also be served as a hand roll</p>
        <p class="item"><b>california</b> crab stick, cucumber &amp; avocado <span class="price">4.5</span></p>
        <p class="item"><b>shrimp</b> cooked shrimp, cucumber &amp; avocado <span class="price">5</span></p>
        <p class="item"><b>crab mix</b> crab salad &amp; avocado <span class="price">5</span></p>
        <p class="item"><b>king crab</b> king crab, cucumber, avocado &amp; sesame seeds <span class="price">8.5</span></p>
        <p class="item"><b>tuna*</b> spicy tuna &amp; avocado <span class="price">5</span></p>
        <p class="item"><b>spicy salmon*</b> spicy salmon &amp; avocado <span class="price">5</span></p>
        <p class="item"><b>smoked salmon</b> smoked salmon &amp; avocado <span class="price">5</span></p>
        <p class="item"><b>spicy scallop*</b> spicy scallops, cucumber &amp; baby sprouts <span class="price">6</span></p>
        <p class="item"><b>hamachi &amp; scallions*</b> yellowtail, scallions &amp; rice wrapped in seaweed <span class="price">4.5</span></p>
        <p class="item"><b>toro &amp; scallions*</b> fatty tuna &amp; scallions <span class="price">m/p</span></p>
        <p class="item"><b>unagi</b> freshwater eel &amp; cucumber <span class="price">5</span></p>
        <p class="item"><b>tekka*</b> tuna &amp; rice wrapped in seaweed <span class="price">4</span></p>
        <p class="item"><b>sake*</b> salmon &amp; rice wrapped in seaweed <span class="price">4</span></p>
        <p class="item"><b>spicy shiro maguro*</b> spicy white tuna, scallions &amp; avocado <span class="price">5</span></p>
        <h2 class="heading"><span>Vegetable Maki</span></h2>
        <p class="item"><b>avocado</b> avocado &amp; rice wrapped in seaweed <span class="price">3</span></p>
        <p class="item"><b>asparagus</b> asparagus &amp; rice wrapped in seaweed <span class="price">3</span></p>
        <p class="item"><b>cucumber</b> cucumber roll topped with sesame seeds <span class="price">3</span></p>
        <p class="item"><b>carrot</b> marinated carrot strips wrapped in rice &amp; seaweed <span class="price">2.5</span></p>
        <p class="item"><b>kampyo</b> sweet gourd &amp; rice wrapped in seaweed <span class="price">3</span></p>
        <p class="item"><b>shiitake</b> mushroom &amp; rice wrapped in seaweed <span class="price">3</span></p>
        <p class="item"><b>oshinko</b> pickled daikon &amp; rice wrapped in seaweed <span class="price">2.5</span></p>
        <p class="item"><b>cucumber &amp; avocado</b> cucumber &amp; avocado roll topped with sesame seeds <span class="price">3.5</span></p>
        <h2 class="heading"><span>Sides</span></h2>
        <div class="smalllist">
          <p class="item"><b>cucumber wrap</b> <span class="price">2</span></p>
          <p class="item"><b>soy paper</b> <span class="price">1</span></p>
          <p class="item"><b>spicy sauce</b> <span class="price">0.5</span></p>
          <p class="item"><b>unagi sauce</b> <span class="price">0.5</span></p>
          <p class="item"><b>fish eggs*</b> <span class="price">1.5</span></p>
          <p class="item"><b>tobiko*</b> <span class="price">2</span></p>
        </div>
      </div>

      <div class="col">
        <header class="brand">
          <div class="brand__mark"></div>
          <div class="brand__name">KAIDO</div>
          <div class="brand__sub">SUSHI BAR</div>
        </header>
        <h2 class="heading"><span>Nigiri &amp; Sashimi</span></h2>
        <p class="note">(priced per pc.)</p>
        <div class="pairs">
          <span>maguro</span><span class="p">2.5</span><span>tuna*</span><span class="p">2.5</span>
          <span>toro</span><span class="p">m/p</span><span>fatty tuna*</span><span class="p">m/p</span>
          <span>shiro maguro</span><span class="p">2.5</span><span>white tuna*</span><span class="p">2.5</span>
          <span>hamachi</span><span class="p">2.5</span><span>yellowtail*</span><span class="p">2.5</span>
          <span>sake</span><span class="p">2.5</span><span>salmon*</span><span class="p">2.5</span>
          <span>kunsei sake</span><span class="p">2.5</span><span>smoked salmon</span><span class="p">2.5</span>
          <span>saba</span><span class="p">2</span><span>mackerel*</span><span class="p">2</span>
          <span>tai</span><span class="p">2.5</span><span>red snapper*</span><span class="p">2.5</span>
          <span>ebi</span><span class="p">2</span><span>shrimp</span><span class="p">2</span>
          <span>ama ebi</span><span class="p">3</span><span>sweet shrimp*</span><span class="p">3</span>
          <span>hokkigai</span><span class="p">2</span><span>surf clam</span><span class="p">2</span>
          <span>kani</span><span class="p">1.5</span><span>crab stick</span><span class="p">1.5</span>
          <span>taraba kani</span><span class="p">3.5</span><span>king crab</span><span class="p">3.5</span>
          <span>tako</span><span class="p">2</span><span>octopus</span><span class="p">2</span>
          <span>hotate</span><span class="p">2.5</span><span>scallop*</span><span class="p">2.5</span>
          <span>unagi</span><span class="p">3</span><span>fresh water eel</span><span class="p">3</span>
          <span>inari</span><span class="p">1.5</span><span>fried tofu</span><span class="p">1.5</span>
          <span>tamago</span><span class="p">1.5</span><span>japanese omelette</span><span class="p">1.5</span>
          <span>ika</span><span class="p">2</span><span>squid*</span><span class="p">2</span>
          <span>masago</span><span class="p">2</span><span>smelt roe*</span><span class="p">2</span>
          <span>tobiko</span><span class="p">2.5</span><span>flying fish egg*</span><span class="p">2.5</span>
          <span>ikura</span><span class="p">3</span><span>salmon roe*</span><span class="p">3</span>
          <span>uni</span><span class="p">4</span><span>sea urchin*</span><span class="p">4</span>
          <span>spicy hotate</span><span class="p">3</span><span>spicy scallop*</span><span class="p">3</span>
        </div>
        <h2 class="heading"><span>Combination</span></h2>
        <p class="note">all combinations served with soup &amp; salad</p>
        <p class="item"><b>omakase special*</b> 8 pcs nigiri &amp; 1 california roll <span class="price">18</span></p>
        <p class="item"><b>omakase deluxe*</b> 10 pcs nigiri &amp; 1 spicy tuna roll <span class="price">22</span></p>
        <p class="item"><b>sake sashimi*</b> 10 pcs salmon sashimi <span class="price">18</span></p>
        <p class="item"><b>tekka sashimi*</b> 10 pcs tuna sashimi <span class="price">20</span></p>
        <p class="item"><b>hamachi sashimi*</b> 10 pcs yellowtail sashimi <span class="price">20</span></p>
        <p class="item"><b>sashimi moriwase*</b> 14/18 pcs of assorted sashimi <span class="price">22/29</span></p>
        <p class="item"><b>sake don*</b> salmon sashimi over rice <span class="price">19</span></p>
        <p class="item"><b>tekka don*</b> tuna sashimi over rice <span class="price">20</span></p>
        <p class="item"><b>unagi don</b> freshwater eel, rice &amp; sauce <span class="price">20</span></p>
        <p class="item"><b>maki combo*</b> california, tuna &amp; salmon rolls <span class="price">10</span></p>
        <p class="item"><b>spicy maki combo*</b> spicy california, spicy tuna &amp; spicy salmon rolls <span class="price">13</span></p>
        <p class="item"><b>chirashi*</b> assorted raw fish &amp; vegetables served over rice <span class="price">20</span></p>
        <p class="item"><b>mixed spicy chirashi bowl*</b> assorted raw fish served on rice &amp; lettuce topped with seaweed, radish, cucumber, tobiko &amp; a quail egg <span class="price">18</span></p>
      </div>
    </div>
    <p class="disclaimer">*These foods contain raw seafood. Consuming raw or partially cooked seafood may increase your risk of foodborne illness. Prices subject to change.</p>
    <div class="photo-strip" role="img" aria-label="Photographs of sashimi, salmon rolls and shrimp nigiri plated on white dishes"></div>
  </section>

</main>
</body>
</html>
```